Design website home page for pathology consulting company

Starting a new consulting company with anatomic pathologists focused on expert diagnosis and second opinions on difficult pathology cases. In the near future we will be incorporating next generation diagnostics for rare diseases of childhood into the business. These include discovery and testing of DNA for mutations.

The company is formed around one of the best known pathologists in the world named Marcus "Buddy" Halvorsen. The name of the company is "BuddyScope"

We had a logo design by Sketchfold - it is great. I will attach file as soon as I have it (contest ending today). Our company is medical, uses microscopes, DNA, probably will focus on childhood diseases but not solely on childhood diseases. we're not particularly conservative, but the customers we want to appeal to include older practicing pathologists as well as patients (sometimes parents) looking for second opinions.

Think a group of expert doctors diagnosing disease through the microscope and through DNA technology, ages ranging from 35-75 all trained by the best pathologist in the world - "Buddy"

We receive glass slides from diseases from patients all over the world from docs who need an expert to tell them what is the diagnosis. So "path to the diagnosis" is also part of the company marketing message.

We want the website design to describe our company but be very simple to find what one is looking for as we will use it as the launch page to:
1) order services
2) check results/reports
3) set up new account
4) speak with one of the pathologists
5) see our test menu
6) access our educational material/webinars

Update - looking for home page design and then finalists will ask for second page design to keep with theme - ok?

Reason: realized this project isn't web design but web home page design - thanks

Reason: Holidays for some in next two weeks

Reason: Hot discussion among collaborators for a few of the submissions. Will provide detail individually this weekend. Thanks so much for all the submissions!

Target Market(s)

Referring pathologists, physicians who want second opinions on pathology disease diagnosis, patients who have had biopsies (either patients themselves or parents of patients), generally high education level

Industry/Entity Type

Marketing

Requirements
Must have
• BuddyScope
Next Generation Pathology Consultants

```html
<!DOCTYPE html>
<html lang="en">
<head>
<meta charset="utf-8">
<title>BuddyScope – Pathology Consultants</title>
<link rel="stylesheet" href="https://fonts.googleapis.com/css2?family=Arimo:wght@400&family=PT+Sans:wght@400&display=swap">
<style>
  :root {
    --ink: #000000;
    --brand: #0a69b0;
    --brand-deep: #0a5590;
    --band: #0b68ad;
    --paper: #e2e2e2;
    --field: #e6e6e6;
    --white: #ffffff;
    --muted: #6b6b6b;
    --soft: #d6d6d6;
    --dark-text: #111111;
  }
  * { box-sizing: border-box; margin: 0; padding: 0; }
  h1, h2, h3 { font-weight: 400; }
  a { text-decoration: none; }
  html, body { width: 1200px; height: 1000px; overflow: hidden; background: var(--ink); }
  body { position: relative; font-family: "PT Sans", Arial, sans-serif; }
  .abs { position: absolute; }

  /* header */
  .site-header { position: absolute; left: 0; top: 0; width: 1200px; height: 475px; background: var(--ink); }
  .brand { left: 145px; top: 80px; display: flex; align-items: center; gap: 10px; }
  .brand-dot { width: 36px; height: 36px; border-radius: 50%; background: var(--brand); }
  .brand-name { font-family: "PT Sans", sans-serif; font-size: 28px; color: var(--brand); line-height: 1; }

  .main-nav { left: 538px; top: 25px; display: flex; }
  .nav-tile { width: 78px; height: 106px; background: var(--brand); margin-right: 7.5px; position: relative;
    color: var(--white); font-family: Arimo, sans-serif; font-size: 13px; text-align: center; }
  .nav-tile svg { position: absolute; left: 50%; top: 20px; transform: translateX(-50%); }
  .nav-tile span { position: absolute; left: 0; right: 0; top: 73px; white-space: nowrap; }
  .nav-tile.is-active { color: var(--ink); }
  .nav-tile.is-active::before { content: ""; position: absolute; left: 0; right: 0; top: -4px; height: 3px; background: #bdbdbd; }

  .hero-kicker { left: 146px; top: 210px; font-size: 17px; color: var(--white); }
  .hero-title { left: 145px; top: 230px; font-size: 40px; line-height: 44px; color: var(--brand); }
  .hero-copy { left: 145px; top: 293px; width: 470px; font-family: Arimo, sans-serif; font-size: 13px; line-height: 20.5px; color: #e4e4e4; }
  .hero-more { left: 146px; top: 391px; font-size: 10px; color: var(--brand); letter-spacing: .3px; }
  .hero-visual { left: 590px; top: 140px; width: 380px; height: 270px;
    background: radial-gradient(ellipse 45% 42% at 50% 50%, #e63bd0 0%, #9d1890 40%, #3a0535 70%, rgba(0,0,0,0) 100%); }
  .slider-dots { left: 535px; top: 437px; display: flex; gap: 5px; }
  .slider-dots i { width: 11px; height: 10px; background: var(--white); display: block; }
  .slider-dots i.is-current { background: var(--brand); }

  /* search band */
  .search-band { left: 0; top: 475px; width: 1200px; height: 63px; background: var(--band); }
  .search-label { left: 146px; top: 23px; font-size: 16px; color: var(--white); letter-spacing: .3px; }
  .search-field { left: 302px; top: 16px; width: 236px; height: 31px; background: var(--field); }
  .search-button { left: 540px; top: 16px; width: 30px; height: 31px; background: var(--brand-deep); }
  .search-button svg { position: absolute; left: 7px; top: 7px; }
  .call-icon { left: 640px; top: 16px; }
  .call-number { left: 697px; top: 12px; font-size: 20px; color: var(--white); }
  .call-link { left: 698px; top: 38px; font-size: 10px; color: var(--white); text-decoration: underline; }

  /* content */
  .content { left: 0; top: 538px; width: 1200px; height: 374px; background: var(--paper); }
  .section-title { font-size: 17px; color: var(--dark-text); }
  .view-all { font-size: 10px; color: var(--brand); text-decoration: underline; }
  .item-title { font-size: 13px; color: var(--brand); }
  .item-text { font-size: 9.5px; line-height: 11.5px; color: var(--muted); }
  .date-tag { width: 77px; height: 21px; background: var(--brand); color: var(--white); font-size: 7.5px; text-align: center; line-height: 21px; }
  .news-rule { left: 145px; width: 425px; height: 1px; background: var(--soft); }
  .case-frame { width: 86px; height: 86px; background: var(--white); }
  .case-frame .case-visual { position: absolute; left: 8px; top: 8px; width: 70px; height: 70px;
    background: linear-gradient(135deg, #7fb6dd 0%, #9fd3ee 45%, #5a5fae 100%); }
  .detail-link { font-size: 10px; color: var(--brand); text-decoration: underline; }

  /* footer */
  .site-footer { left: 0; top: 912px; width: 1200px; height: 88px; background: var(--ink); }
  .follow-box { left: 146px; top: -5px; width: 145px; height: 93px; background: var(--brand); }
  .follow-box::after { content: ""; position: absolute; right: -5px; top: 0; border-left: 5px solid var(--brand-deep); border-top: 5px solid transparent; }
  .follow-title { left: 17px; top: 26px; font-size: 13px; color: var(--white); }
  .follow-rule { left: 17px; top: 47px; width: 110px; height: 1px; background: #3d85c0; }
  .social { top: 54px; width: 27px; height: 27px; border-radius: 50%; }
  .footer-nav { left: 393px; top: 46px; font-size: 10px; color: var(--white); white-space: nowrap; }
  .footer-nav .sep { margin: 0 6px; }
  .footer-nav .is-active { color: var(--brand); }
  .footer-brand { right: 242px; top: 34px; display: flex; align-items: center; gap: 5px; }
  .footer-brand .brand-dot { width: 16px; height: 16px; }
  .footer-brand .brand-name { font-size: 14px; }
  .copyright { right: 242px; top: 67px; font-size: 8px; color: var(--white); text-align: right; }
</style>
</head>
<body>

<header class="site-header">
  <div class="abs brand"><span class="brand-dot"></span><span class="brand-name">BuddyScope</span></div>

  <nav class="abs main-nav">
    <a class="nav-tile is-active">
      <svg width="44" height="44" viewBox="0 0 44 44"><circle cx="22" cy="22" r="22" fill="#000"/><circle cx="23.5" cy="12" r="3" fill="#0a69b0"/><path d="M19 18h7l-3 15h3l-1 3h-8l1-3h2l2-12h-3z" fill="#0a69b0"/></svg>
      <span>About Us</span>
    </a>
    <a class="nav-tile">
      <svg width="36" height="44" viewBox="0 0 36 44" fill="#d9d9d9"><rect x="13" y="2" width="7" height="18" rx="1" transform="rotate(-20 16 11)"/><rect x="12" y="22" width="10" height="3"/><path d="M24 14a12 12 0 0 1 0 22h-4v-3h4a9 9 0 0 0 0-16z"/><rect x="6" y="36" width="26" height="5" rx="1"/><rect x="14" y="27" width="8" height="9"/></svg>
      <span>Our Team</span>
    </a>
    <a class="nav-tile">
      <svg width="40" height="44" viewBox="0 0 40 44" fill="none" stroke="#d9d9d9" stroke-width="2.5"><path d="M8 3h20l8 8v30H8z"/><path d="M28 3v8h8"/><path d="M14 16h16M14 22h16M14 28h10"/><path d="M4 30l4 5 7-9"/></svg>
      <span>Reports</span>
    </a>
    <a class="nav-tile">
      <svg width="44" height="44" viewBox="0 0 44 44"><g fill="#d9d9d9"><circle cx="22" cy="22" r="15"/><g id="teeth"><rect x="18.5" y="1" width="7" height="8"/><rect x="18.5" y="35" width="7" height="8"/><rect x="1" y="18.5" width="8" height="7"/><rect x="35" y="18.5" width="8" height="7"/></g><use href="#teeth" transform="rotate(45 22 22)"/></g><circle cx="22" cy="22" r="6" fill="#0a69b0"/></svg>
      <span>Services</span>
    </a>
    <a class="nav-tile">
      <svg width="44" height="44" viewBox="0 0 44 44" fill="none" stroke="#d9d9d9" stroke-width="2.5"><circle cx="22" cy="22" r="20"/><path d="M16 11l4 6-3 3c1 3 4 6 7 7l3-3 6 4-3 4c-8 0-17-9-17-17z" fill="#d9d9d9" stroke="none"/></svg>
      <span>Contact Us</span>
    </a>
  </nav>

  <p class="abs hero-kicker">Welcome To</p>
  <h1 class="abs hero-title">BuddyScope</h1>
  <p class="abs hero-copy">Lorem Ipsum is simply dummy text of the printing and typesetting industry. Lorem Ipsum has been the industry's standard dummy text ever since the 1500s, when an unknown printer took a galley of type and scrambled it to make a type specimen book.</p>
  <a class="abs hero-more">read more about us....</a>
  <div class="abs hero-visual" role="img" aria-label="Glowing magenta capsule containing a DNA double helix"></div>
  <div class="abs slider-dots"><i class="is-current"></i><i></i><i></i><i></i></div>
</header>

<section class="abs search-band">
  <span class="abs search-label">SEARCH OUR SITE</span>
  <div class="abs search-field"></div>
  <div class="abs search-button"><svg width="17" height="17" viewBox="0 0 17 17" fill="none" stroke="#dfe9f2" stroke-width="2"><circle cx="6.5" cy="6.5" r="5"/><path d="M10 10l6 6" stroke-width="3"/></svg></div>
  <svg class="abs call-icon" width="32" height="32" viewBox="0 0 44 44" fill="none" stroke="#fff" stroke-width="2.5"><circle cx="22" cy="22" r="20"/><path d="M16 11l4 6-3 3c1 3 4 6 7 7l3-3 6 4-3 4c-8 0-17-9-17-17z" fill="#fff" stroke="none"/></svg>
  <span class="abs call-number">555 014 27300</span>
  <a class="abs call-link">Click Here to Contact Us</a>
</section>

<main class="abs content">
  <h2 class="abs section-title" style="left:146px;top:48px">Latest News &amp; Announcement</h2>
  <a class="abs view-all" style="left:146px;top:70px">View All</a>

  <h3 class="abs item-title" style="left:146px;top:102px">Lorem Ipsum is simply dummy text</h3>
  <div class="abs date-tag" style="left:494px;top:100px">October 14, 2013</div>
  <p class="abs item-text" style="left:146px;top:128px;width:425px">Lorem Ipsum is simply dummy text of the printing and typesetting industry. Lorem Ipsum has been the industry's standard dummy text ever since</p>
  <div class="abs news-rule" style="top:163px"></div>

  <h3 class="abs item-title" style="left:146px;top:174px">Lorem Ipsum is simply dummy text</h3>
  <div class="abs date-tag" style="left:494px;top:173px">October 14, 2013</div>
  <p class="abs item-text" style="left:146px;top:200px;width:425px">Lorem Ipsum is simply dummy text of the printing and typesetting industry. Lorem Ipsum has been the industry's standard dummy text ever since</p>

  <h2 class="abs section-title" style="left:640px;top:48px">Case In Focus</h2>
  <a class="abs view-all" style="left:641px;top:70px">View All</a>

  <div class="abs case-frame" style="left:640px;top:104px"><div class="case-visual" role="img" aria-label="Molecular structure model in blue and violet"></div></div>
  <h3 class="abs item-title" style="left:738px;top:102px">Lorem Ipsum is simply</h3>
  <p class="abs item-text" style="left:738px;top:128px;width:220px">Lorem Ipsum is simply dummy text of the printing and typesetting industry. Lorem Ipsum has been the industry's standard dummy text ever since</p>
  <a class="abs detail-link" style="left:738px;top:176px">View Detail</a>

  <div class="abs case-frame" style="left:640px;top:220px"><div class="case-visual" role="img" aria-label="Molecular structure model in blue and violet"></div></div>
  <h3 class="abs item-title" style="left:738px;top:218px">Lorem Ipsum is simply</h3>
  <p class="abs item-text" style="left:738px;top:246px;width:220px">Lorem Ipsum is simply dummy text of the printing and typesetting industry. Lorem Ipsum has been the industry's standard dummy text ever since</p>
  <a class="abs detail-link" style="left:738px;top:294px">View Detail</a>
</main>

<footer class="abs site-footer">
  <div class="abs follow-box">
    <span class="abs follow-title">Follow Us</span>
    <div class="abs follow-rule"></div>
    <span class="abs social" style="left:17px;background:#2b2b2b"></span>
    <span class="abs social" style="left:52px;background:#1a8ad8"></span>
    <span class="abs social" style="left:86px;background:#1a8ad8"></span>
  </div>
  <nav class="abs footer-nav"><span class="is-active">About Us</span><span class="sep">|</span>Our Team<span class="sep">|</span>Report<span class="sep">|</span>Services<span class="sep">|</span>Cntact Us<span class="sep">|</span>Privacy<span class="sep">|</span>Terms</nav>
  <div class="abs footer-brand"><span class="brand-dot"></span><span class="brand-name">BuddyScope</span></div>
  <p class="abs copyright">All Right Reserved Copyright BuddyScope.</p>
</footer>

</body>
</html>
```